We need a PowerPoint to outline what Modeling is about!

PowerPoint presentation to be shown to aspiring models. The students will be joining our 1-day workshop, and they will be taught the very basics of being a model.
What should be included in the slides:
• What is Modelling? - Description of Modelling, and what it takes to be a Model.
• Types of Models in the market - Catwalk Model / Photography Model / Events Model
• Expectations of a model - Professionalism, Punctuality, Confidence, etc etc.
• Practical (catwalk) tips: Posture
• Practical (catwalk) tips: How to do a simple catwalk
• Practical (photography) tips: How to bring out your best angles in photos
• Trainer Assessment of Students
Here are some definitions that we use. You may change the wording as you see fit, as long as the meaning is the same.
Modelling is to promote a product / brand / service in an advertisement, show, commercial or event.
Runway / Fashion Model – Walk the catwalk to promote clothing and accessories in a fashion show.
Most shows require the model to be tall and skinny. Model needs to strut with confidence and grace down the runway. Body shape more important than facial features.
Photography Model – Appear for Print Ads, Magazine Editorials, Posters, etc.
Height requirements are not as strict (or not present) as compared to Runway Model. Good features preferred, but not a must.
Video Model – Appear for TV commercials, Promotional Videos, etc.
Model needs to possess basic acting skills to promote the product, brand or service on video. Confidence and screen charisma more important than looks or body.
Events Model – Promote the product, brand or service during ‘live’ events and shows.
Model needs to be engaging and charismatic to ‘sell’ the product to customers.
A longer description can also be found here: http://www.brightlarkagency.sg/models/
Target Market(s)
Adults aged 18 - 40 who are interested to take up Modeling.
Industry/Entity Type
Events
Requirements
Must have
- Visually appealing! Does not have to be content heavy, but should deliver the message effectively.
Nice to have
- Pretty pictures.

```html
<!DOCTYPE html>
<html lang="en">
<head>
<meta charset="utf-8">
<title>What It Takes To Be A Model?</title>
<link rel="stylesheet" href="https://fonts.googleapis.com/css2?family=Federo&family=Abel&display=swap">
<style>
  :root {
    --paper: #fdfbfd;
    --ink: #111111;
    --accent-pink: #ee1a62;
    --block-black: #000000;
    --figure-dark: #1a1a1a;
    --figure-light: #e9e6e9;
    --star: #6a6a6a;
  }
  html, body {
    margin: 0;
    padding: 0;
    overflow: hidden;
    background: var(--paper);
  }
  .slide {
    position: relative;
    width: 1200px;
    height: 900px;
    background: var(--paper);
    overflow: hidden;
  }
  .accent-bar {
    position: absolute;
    left: 0;
    top: 0;
    width: 492px;
    height: 38px;
    background: var(--accent-pink);
  }
  .slide-title {
    position: absolute;
    left: 470px;
    top: 72px;
    width: 710px;
    margin: 0;
    font-family: "Federo", sans-serif;
    font-weight: 400;
    font-size: 66px;
    line-height: 76px;
    letter-spacing: 6px;
    text-align: center;
    text-transform: uppercase;
    color: var(--ink);
  }
  .corner-block {
    position: absolute;
    left: 1090px;
    top: 243px;
    width: 110px;
    height: 138px;
    background: var(--block-black);
  }
  .figure-illustration {
    position: absolute;
    left: 0;
    top: 170px;
    width: 265px;
    height: 730px;
    background: linear-gradient(100deg, var(--figure-dark) 0%, var(--figure-dark) 45%, var(--figure-light) 75%, var(--paper) 100%);
    opacity: 0.9;
  }
  .requirements {
    position: absolute;
    left: 272px;
    top: 460px;
    margin: 0;
    padding: 0;
    list-style: none;
    font-family: "Abel", sans-serif;
    font-size: 33.5px;
    color: var(--ink);
  }
  .requirements li {
    display: flex;
    align-items: center;
    height: 45.6px;
    white-space: nowrap;
  }
  .requirements .bullet-star {
    width: 30px;
    height: 30px;
    margin-right: 24px;
    flex: none;
  }
  .agency-name {
    position: absolute;
    right: 22px;
    bottom: 48px;
    display: flex;
    align-items: center;
    gap: 10px;
    font-family: "Abel", sans-serif;
    font-size: 20px;
    color: var(--ink);
    white-space: nowrap;
  }
  .agency-name .agency-square {
    width: 12px;
    height: 12px;
    background: var(--ink);
    flex: none;
  }
</style>
</head>
<body>
<main class="slide">
  <div class="accent-bar"></div>
  <h1 class="slide-title">What it takes to<br>be a model?</h1>
  <div class="corner-block"></div>
  <div class="figure-illustration" role="img" aria-label="Stylised illustration of a woman with curly black hair in a black strapless gown"></div>

  <svg width="0" height="0" style="position:absolute">
    <defs>
      <symbol id="star" viewBox="0 0 30 30">
        <path d="M15 3 L16.3 13.7 L27 15 L16.3 16.3 L15 27 L13.7 16.3 L3 15 L13.7 13.7 Z" fill="var(--star)"/>
        <path d="M7 7 L23 23 M23 7 L7 23" stroke="var(--star)" stroke-width="1"/>
      </symbol>
    </defs>
  </svg>

  <ul class="requirements">
    <li><svg class="bullet-star"><use href="#star"/></svg>A slim build</li>
    <li><svg class="bullet-star"><use href="#star"/></svg>A height somewhere between 5'8" and 5'11" (there&nbsp; are exceptions)</li>
    <li><svg class="bullet-star"><use href="#star"/></svg>Good bone structure with a symmetrical and angulaface</li>
    <li><svg class="bullet-star"><use href="#star"/></svg>Being naturally photogenic and/or a good knowledge of on“angles”</li>
    <li><svg class="bullet-star"><use href="#star"/></svg>Good posture and a strong runway walk (learned or natural)</li>
    <li><svg class="bullet-star"><use href="#star"/></svg>Confidence</li>
    <li><svg class="bullet-star"><use href="#star"/></svg>Strong personality</li>
    <li><svg class="bullet-star"><use href="#star"/></svg>Photogenecity</li>
  </ul>

  <div class="agency-name"><span class="agency-square"></span>Brightlark Agency</div>
</main>
</body>
</html>
```